School Management website

I need page design for our school management system website

Base website is www.tavrinel.com. When the student logs in, he will reach the below pages.
You can either design with white and blue background or grey and white background

Page 1 - School Info

Header
product name("Tavrinel") in left corner
logout link in right corner

LeftMenu

Dashboard
School Info
School Settings
Staffs
Classes
Messaging
Contact Us

Footer
About link and copyright text

School Info content
The page should have breadcrumb

The content of this page will be the school profile
We have to show the school logo
Name
School Type
School Code
School Count
School Address
School phone 1&2
School Email
School Website

The page content should show edit school profile link which will take the user to another page

```html
<!DOCTYPE html>
<html lang="en">
<head>
<meta charset="utf-8">
<title>Tavrinel – Dashboard</title>
<link href="https://fonts.googleapis.com/css2?family=Arimo:wght@400;700&family=Source+Sans+3:wght@700&display=swap" rel="stylesheet">
<style>
  :root{
    --blue:#29a8e0;
    --blue-light:#7fd0f2;
    --ink:#333333;
    --body-text:#3c3c3c;
    --muted:#a9a9a9;
    --field-bg:#f4f4f4;
    --field-edge:#d9d9d9;
    --rule:#e2e2e2;
    --footer:#3f3f3f;
    --white:#ffffff;
  }
  *{box-sizing:border-box;margin:0;padding:0}
  html,body{width:1200px;height:725px;overflow:hidden}
  body{font-family:"Arimo",Arial,sans-serif;background:var(--white);color:var(--ink);position:relative}

  .site-header{position:absolute;left:0;top:0;width:1200px;height:134px;background:var(--white)}
  .brand{position:absolute;left:110px;top:44px;display:flex;align-items:center;gap:10px;
    font-family:"Arimo",Arial,sans-serif;font-weight:700;font-size:34px;color:var(--blue);text-decoration:none}
  .brand-mark{width:18px;height:18px;background:var(--blue)}
  .logout{position:absolute;left:1005px;top:46px;width:96px;height:36px;border-radius:5px;
    background:var(--blue);border:1px solid var(--blue-light);box-shadow:inset 0 0 0 1px var(--blue);
    color:var(--white);font-size:17px;line-height:34px;text-align:center;text-decoration:none}

  .stage{position:absolute;left:0;top:134px;width:1200px;height:492px;background:var(--blue)}
  .panel{position:absolute;left:100px;top:18px;width:1000px;height:474px;background:var(--white)}

  .side-menu{position:absolute;left:0;top:0;width:254px;height:474px;border-right:1px solid #e6e6e6;list-style:none;padding-top:20px}
  .side-menu li{position:relative;margin:0 7px 0 20px;height:48px;border-bottom:1px dotted #c8c8c8}
  .side-menu li:last-child{border-bottom:none}
  .side-menu a{position:absolute;left:9px;top:13px;display:flex;align-items:center;gap:8px;
    font-size:15px;letter-spacing:.3px;color:var(--ink);text-decoration:none}
  .side-menu svg{width:17px;height:17px;fill:none;stroke:var(--blue);stroke-width:1.4}

  .content{position:absolute;left:254px;top:0;width:746px;height:474px}
  .breadcrumb{position:absolute;left:8px;top:18px;display:flex;align-items:center;font-size:15px;color:var(--ink)}
  .breadcrumb svg{width:16px;height:17px;fill:none;stroke:var(--blue);stroke-width:1.4;margin-right:7px}
  .breadcrumb .sep{color:var(--blue);font-weight:700;font-size:18px;margin:0 5px 0 18px}
  .section-title{position:absolute;left:6px;top:70px;font-family:"Source Sans 3","Source Sans Pro",sans-serif;
    font-weight:700;font-size:25px;color:var(--blue);letter-spacing:.2px}
  .about{position:absolute;left:14px;top:105px;width:720px;font-size:12.4px;line-height:20px;color:var(--body-text)}
  .about p+p{margin-top:20px}
  .divider{position:absolute;left:8px;top:309px;width:731px;border-top:1px solid var(--rule)}

  .field{position:absolute;height:31px;border-radius:5px;background:var(--field-bg);
    border:1px solid #ececec;box-shadow:inset 0 3px 2px -1px var(--field-edge);
    font-size:12.5px;color:var(--muted);line-height:31px;padding-left:13px}
  .field.select::after{content:"";position:absolute;right:5px;top:13px;border:4px solid transparent;border-top:4px solid #b4b4b4}

  .site-footer{position:absolute;left:0;top:626px;width:1200px;height:99px;background:var(--footer);color:#f2f2f2;text-align:center;font-size:13px}
  .footer-links{position:absolute;top:39px;width:100%;letter-spacing:.2px}
  .footer-links a{color:#f2f2f2;text-decoration:none}
  .footer-links span{margin:0 6px}
  .copyright{position:absolute;top:69px;width:100%;font-size:12.5px}
</style>
</head>
<body>
  <header class="site-header">
    <a class="brand" href="#"><span class="brand-mark"></span>Tavrinel</a>
    <a class="logout" href="#">Logout</a>
  </header>

  <main class="stage">
    <div class="panel">
      <ul class="side-menu">
        <li><a href="#"><svg viewBox="0 0 17 17"><path d="M2 8.5 8.5 2 15 8.5M4 7v8h3.5v-4h2v4H13V7"/></svg>Dashboard</a></li>
        <li><a href="#"><svg viewBox="0 0 17 17"><path d="M9 2H2v13h13V8"/><path d="M7 10l1-3 7-6 2 2-7 6z"/></svg>School Info</a></li>
        <li><a href="#"><svg viewBox="0 0 17 17"><circle cx="8.5" cy="8.5" r="2.5"/><circle cx="8.5" cy="8.5" r="6" stroke-dasharray="3 1.7"/></svg>School Settings</a></li>
        <li><a href="#"><svg viewBox="0 0 17 17"><circle cx="8.5" cy="5" r="3.5"/><path d="M1.5 16v-2c0-2.5 2-4 4-4h6c2 0 4 1.5 4 4v2z"/></svg>Staffs</a></li>
        <li><a href="#"><svg viewBox="0 0 17 17" style="fill:var(--blue);stroke:none"><rect x="1" y="1" width="5" height="5"/><rect x="11" y="4" width="4" height="4"/><circle cx="3" cy="12" r="2"/><circle cx="8.5" cy="12" r="2"/><circle cx="14" cy="12" r="2"/><rect x="1" y="14" width="15" height="3"/></svg>Classes</a></li>
        <li><a href="#"><svg viewBox="0 0 17 17"><path d="M1 3h5l1.5 2H15v9H1z"/><path d="M1 7h14"/></svg>Messaging</a></li>
        <li><a href="#"><svg viewBox="0 0 17 17"><rect x="1" y="3" width="15" height="11"/><path d="M1 3l7.5 6L16 3"/></svg>Contact Us</a></li>
      </ul>

      <section class="content">
        <nav class="breadcrumb">
          <svg viewBox="0 0 16 17"><path d="M1 8.5 8 1.5l7 7M3 7v9h3.5v-5h3v5H13V7"/></svg>
          <span>Home</span><span class="sep">»</span><span>Dashboard</span>
        </nav>

        <h1 class="section-title">WHO WE ARE</h1>
        <div class="about">
          <p>Tavrinel is an online service for the schools to easily manage their school activity. Enables teachers-parents -students communica-tion in a better way. We almost provide all the functionality needed to manage your institutions. The features are developed taking the suggestions and concerns of many top level school managers.</p>
          <p>We will simplify most of your school management activities and will help you to update your school with all the latest technology.</p>
          <p>Our system is completely web based meaning that it can be accessed from any computer using internet access. You can access from anywhere, anytime. Your data are stored in the world class highly secured servers.</p>
        </div>
        <div class="divider"></div>

        <div class="field" style="left:23px;top:338px;width:163px">Name</div>
        <div class="field select" style="left:199px;top:338px;width:163px;padding-left:9px">School Type</div>
        <div class="field" style="left:380px;top:337px;width:163px;padding-left:3px">School Code</div>
        <div class="field select" style="left:549px;top:338px;width:163px;padding-left:8px">School Count</div>
        <div class="field" style="left:23px;top:387px;width:163px">School Address</div>
        <div class="field" style="left:199px;top:387px;width:163px;padding-left:9px">School phone</div>
        <div class="field" style="left:373px;top:387px;width:163px;padding-left:9px">School Email</div>
        <div class="field" style="left:549px;top:387px;width:163px;padding-left:9px">School Website</div>
      </section>
    </div>
  </main>

  <footer class="site-footer">
    <nav class="footer-links">
      <a href="#">Dashboard</a><span>|</span><a href="#">School Info</a><span>|</span><a href="#">School Settings</a><span>|</span><a href="#">Staffs</a><span>|</span><a href="#">Classes</a><span>|</span><a href="#">Messaging</a><span>|</span><a href="#">Contact Us</a>
    </nav>
    <p class="copyright">Copyright © 2014 | All Rights Reserved</p>
  </footer>
</body>
</html>
```